Tarrow Building Performance

Id like for my business card to be very bold and professional. Incorporating the business logo, the main services offered, and my contact info. Services are spray foam, insulation, new construction, retrofit, weatherization.

When opening this project sketch harbor was not able to upload my new logo that I picked from another recent sketch harbor project. Does anyone know how i could upload my logo onto the page for design of the business cards?

Target Market(s)

Building owners, contractors

Industry/Entity Type

Building Insulation and performance improvements

Contact Information for Business Card

Owner, Email dean@tarrowbuildingperformance.example Phone number 555-208-6147

Colors
0054AA
0677BA
7BADD7
CADEEF
E8F1F8
F0912C
F2A743
F7CA91
FBE8D2
FDF5EE

Requirements
Must have
• Services- spray foam, cellulose, mineral wool, fiberglass, air sealing, new construction, retrofit, weatherization, energy saving assesments

```html
<!DOCTYPE html>
<html lang="en">
<head>
<meta charset="utf-8">
<title>Tarrow Building Performance – Business Card</title>
<link rel="stylesheet" href="https://fonts.googleapis.com/css2?family=Poppins:wght@400;500;600;800&display=swap">
<style>
  :root {
    --navy: #0d1d4f;
    --navy-deep: #08153d;
    --orange: #f0912c;
    --orange-light: #f2a743;
    --cyan: #3cc3e4;
    --white: #ffffff;
    --page: #e9ecf1;
  }
  * { box-sizing: border-box; margin: 0; padding: 0; }
  html, body { width: 1200px; height: 917px; overflow: hidden; }
  body {
    background: var(--page);
    font-family: "Poppins", sans-serif;
    position: relative;
  }
  .card {
    position: absolute;
    top: 307px;
    width: 530px;
    height: 303px;
    overflow: hidden;
    border-radius: 4px;
    box-shadow: 0 10px 28px rgba(8, 21, 61, 0.22);
  }
  .card-front { left: 40px; }
  .card-back { left: 630px; background: radial-gradient(ellipse at 60% 40%, #142a6b 0%, var(--navy) 55%, var(--navy-deep) 100%); }

  .front-art { position: absolute; inset: 0; }

  .brand-block {
    position: absolute;
    left: 34px;
    top: 24px;
    color: var(--white);
    line-height: 1;
  }
  .brand-name { font-weight: 800; font-size: 52px; letter-spacing: 1px; }
  .brand-sub { font-weight: 600; font-size: 15px; letter-spacing: 0.5px; margin-top: 4px; }

  .contact-block {
    position: absolute;
    left: 120px;
    top: 168px;
  }
  .person-name { color: var(--orange); font-weight: 800; font-size: 21px; letter-spacing: 0.5px; line-height: 1.05; }
  .person-role { color: var(--cyan); font-weight: 500; font-size: 15px; line-height: 1.2; margin-bottom: 10px; }
  .contact-line {
    display: flex;
    align-items: center;
    gap: 9px;
    color: var(--white);
    font-size: 14px;
    font-weight: 500;
    margin-top: 5px;
  }
  .contact-icon {
    width: 18px; height: 18px;
    border-radius: 50%;
    background: var(--orange);
    display: flex; align-items: center; justify-content: center;
    flex: none;
  }

  .back-brand {
    position: absolute;
    left: 150px;
    top: 58px;
    display: flex;
    align-items: center;
    gap: 12px;
  }
  .back-brand-mark { width: 22px; height: 22px; background: var(--cyan); flex: none; }
  .back-brand-name {
    color: var(--orange);
    font-weight: 800;
    font-size: 22px;
    line-height: 1.1;
    letter-spacing: 0.5px;
  }
  .services-title {
    position: absolute;
    left: 0; right: 0;
    top: 138px;
    text-align: center;
    color: var(--orange);
    font-weight: 800;
    font-size: 17px;
    letter-spacing: 1px;
  }
  .services-list {
    position: absolute;
    left: 0; right: 0;
    top: 170px;
    text-align: center;
    color: var(--white);
    font-size: 14px;
    line-height: 1.75;
  }
  .services-list .dot { color: var(--orange); font-weight: 800; margin: 0 5px; }
</style>
</head>
<body>

  <section class="card card-front" aria-label="Business card front">
    <svg class="front-art" viewBox="0 0 530 303" preserveAspectRatio="none">
      <defs>
        <linearGradient id="orangeFill" x1="0" y1="1" x2="1" y2="0">
          <stop offset="0" stop-color="#e07a1f"/>
          <stop offset="1" stop-color="#f2a743"/>
        </linearGradient>
        <linearGradient id="navyFill" x1="0" y1="0" x2="1" y2="1">
          <stop offset="0" stop-color="#142a6b"/>
          <stop offset="1" stop-color="#08153d"/>
        </linearGradient>
      </defs>
      <rect width="530" height="303" fill="url(#navyFill)"/>
      <polygon points="0,0 530,0 530,60 300,140 0,140" fill="url(#orangeFill)"/>
      <polygon points="0,140 300,140 530,60 530,74 304,154 0,154" fill="var(--cyan)"/>
      <rect x="0" y="291" width="530" height="12" fill="var(--cyan)"/>
    </svg>

    <div class="brand-block">
      <div class="brand-name">TARROW</div>
      <div class="brand-sub">BUILDING PERFORMANCE</div>
    </div>

    <div class="contact-block">
      <div class="person-name">DEAN MARLOWE</div>
      <div class="person-role">Owner</div>
      <div class="contact-line">
        <span class="contact-icon">
          <svg width="10" height="10" viewBox="0 0 24 24"><path fill="#0d1d4f" d="M6.6 10.8a15.1 15.1 0 0 0 6.6 6.6l2.2-2.2a1 1 0 0 1 1-.25 11.4 11.4 0 0 0 3.6.57 1 1 0 0 1 1 1V20a1 1 0 0 1-1 1A17 17 0 0 1 3 4a1 1 0 0 1 1-1h3.5a1 1 0 0 1 1 1c0 1.25.2 2.45.57 3.57a1 1 0 0 1-.25 1z"/></svg>
        </span>
        555-208-6147
      </div>
      <div class="contact-line">
        <span class="contact-icon">
          <svg width="10" height="10" viewBox="0 0 24 24"><path fill="#0d1d4f" d="M2 5h20v14H2z"/><path fill="none" stroke="#f0912c" stroke-width="2" d="M2 6l10 7 10-7"/></svg>
        </span>
        dean@tarrowbuildingperformance.example
      </div>
    </div>
  </section>

  <section class="card card-back" aria-label="Business card back">
    <div class="back-brand">
      <span class="back-brand-mark"></span>
      <div class="back-brand-name">TARROW<br>BUILDING PERFORMANCE</div>
    </div>

    <div class="services-title">SERVICES</div>
    <div class="services-list">
      <div><span class="dot">•</span>spray foam<span class="dot">•</span>cellulose<span class="dot">•</span>mineral wool<span class="dot">•</span>fiberglass</div>
      <div><span class="dot">•</span>air sealing<span class="dot">•</span>new construction<span class="dot">•</span>retrofit<span class="dot">•</span>weatherization</div>
      <div><span class="dot">•</span>energy saving assesments</div>
    </div>
  </section>

</body>
</html>
```